Boutique Soy Candle Company Needs a Label Design

We need a label design for a boutique soy candle company based in Venner Bay, South Australia.
We sell high quality, hand poured soy wax candles, melts and reed diffusers.
We are based in a coastal town and would like the label to reflect our rustic, beachy, retro but luxurious feel. I've attached the design we've been using and like the idea but want to have something more professional. The picture of the Venner Spire is something that we would like to be included somehow - it's like our town symbol - a 'lighthouse' of sorts. It was quite stylised on my original design but we are open to different interpretations.
We like the idea of a 'Kraft' brown paper sort of label but are not set on it. We also love the fluro pink look.

```html
<!DOCTYPE html>
<html lang="en">
<head>
<meta charset="utf-8">
<title>Glowmere Soy Candle Labels</title>
<link rel="stylesheet" href="https://fonts.googleapis.com/css2?family=Oswald:wght@500;700&family=Josefin+Sans:wght@600;700&display=swap">
<style>
  :root {
    --backdrop: #e9ecee;
    --ink: #2a2226;
    --mint: #eaf5d9;
    --apricot: #fbb86c;
    --tangerine: #f26a1f;
    --paper: #ffffff;
    --fluro-pink: #e27ae9;
    --rule: #231f20;
  }
  * { box-sizing: border-box; margin: 0; padding: 0; }
  html, body {
    width: 1200px;
    height: 875px;
    overflow: hidden;
    background: var(--backdrop);
  }
  .label-sheet {
    position: relative;
    width: 1200px;
    height: 875px;
  }
  .label {
    position: absolute;
    top: 212px;
    width: 530px;
    height: 450px;
    overflow: hidden;
    box-shadow: 0 2px 8px rgba(0,0,0,0.12);
  }
  .label--apricot { left: 55px; background: var(--mint); }
  .label--pink { left: 615px; background: var(--paper); }

  .label__brand {
    position: absolute;
    top: 70px;
    left: 0;
    width: 100%;
    text-align: center;
    font-family: "Oswald", sans-serif;
    font-weight: 700;
    font-size: 84px;
    line-height: 1;
    color: var(--ink);
  }

  .label__band {
    position: absolute;
    background: var(--apricot);
  }
  .label--apricot .label__band { left: 0; top: 212px; width: 530px; height: 238px; }
  .label--pink .label__band {
    left: 32px; top: 212px; width: 470px; height: 212px;
    background: var(--fluro-pink);
    border-radius: 14px 30px 34px 22px;
  }

  .label__spire {
    position: absolute;
    left: 140px;
    top: 212px;
    width: 30px;
    height: 68px;
    background: var(--ink);
  }

  .rule { position: absolute; background: var(--rule); }
  .rule--vertical { left: 225px; top: 246px; width: 2px; height: 178px; }
  .rule--upper { left: 90px; top: 285px; width: 412px; height: 2px; }
  .rule--lower { left: 90px; top: 372px; width: 412px; height: 2px; }

  .weight {
    position: absolute;
    left: 90px;
    top: 298px;
    width: 135px;
    text-align: center;
    font-family: "Josefin Sans", sans-serif;
    font-weight: 700;
    color: var(--ink);
    line-height: 1;
  }
  .weight__amount { display: block; font-size: 40px; }
  .weight__unit { display: block; font-size: 19px; margin-top: 2px; }

  .origin {
    position: absolute;
    left: 238px;
    top: 257px;
    font-family: "Josefin Sans", sans-serif;
    font-weight: 600;
    font-size: 18px;
    line-height: 1.2;
    color: var(--ink);
    white-space: nowrap;
  }
  .claim {
    position: absolute;
    left: 238px;
    top: 308px;
    font-family: "Oswald", sans-serif;
    font-weight: 500;
    font-size: 34px;
    line-height: 1;
    letter-spacing: 1px;
    color: var(--tangerine);
    white-space: nowrap;
  }
  .label--pink .claim { color: var(--paper); }

  .batch {
    position: absolute;
    left: 90px;
    top: 388px;
    width: 135px;
    text-align: center;
    font-family: "Josefin Sans", sans-serif;
    font-weight: 600;
    font-size: 21px;
    line-height: 1.2;
    color: var(--ink);
  }
  .scent {
    position: absolute;
    left: 238px;
    top: 389px;
    font-family: "Josefin Sans", sans-serif;
    font-weight: 600;
    font-size: 19px;
    line-height: 1.2;
    color: var(--ink);
    white-space: nowrap;
  }
</style>
</head>
<body>
<main class="label-sheet">

  <section class="label label--apricot">
    <h1 class="label__brand">glowmere</h1>
    <div class="label__band"></div>
    <div class="label__spire" role="img" aria-label="Stylised Venner Spire landmark illustration"></div>
    <div class="rule rule--vertical"></div>
    <div class="rule rule--upper"></div>
    <div class="rule rule--lower"></div>
    <p class="weight"><span class="weight__amount">300</span><span class="weight__unit">GRAMS</span></p>
    <p class="origin">Hand made in Venner Bay, SA</p>
    <p class="claim">ALL NATURAL SOY</p>
    <p class="batch">no. 004</p>
    <p class="scent">Honey Suckle Jasmine</p>
  </section>

  <section class="label label--pink">
    <h1 class="label__brand">glowmere</h1>
    <div class="label__band"></div>
    <div class="label__spire" role="img" aria-label="Stylised Venner Spire landmark illustration"></div>
    <div class="rule rule--vertical"></div>
    <div class="rule rule--upper"></div>
    <div class="rule rule--lower"></div>
    <p class="weight"><span class="weight__amount">300</span><span class="weight__unit">GRAMS</span></p>
    <p class="origin">Hand made in Venner Bay, SA</p>
    <p class="claim">ALL NATURAL SOY</p>
    <p class="batch">no. 004</p>
    <p class="scent">Honey Suckle Jasmine</p>
  </section>

</main>
</body>
</html>
```